Morning Harbor Bible Fellowship needs a new Business Card/Letterhead Suite

***** IT DOES NOT HAVE TO FEATURE GREEN AND BROWN in order to be a successful design*****

****FONTS: SF New Republic, 'Morning Harbor'; Nexa Light, 'Bible Fellowship'****

***We have two locations, with two addresses. So the business card AND letterhead need to include two sets of address information***

We are a growing church in New York in need of a new stationary suite. We have recently adopted a new logo (via a successful ArtHivePro project) and need new business cards, letterhead, envelopes, and folders.

We would like to see creative, original designs that are modern and clean/elegant (NOT dated "churchy" graphics that are cheesy).

We need this project worked on immediately, as we need to print new business cards for upcoming programs we have on our schedule. So, the designs need to be solid so that we can move quickly throughout the revision process toward print.

We'd also need editables files, so that we can drop in other staff members names/phone numbers, to be able to print cards for those staff needing them.

Requirements
Must have
• Our logo
• Must be given to us in an editable format (to change names)
Nice to have
• Some examples on grey, or recycled, card stock
• card stock (background) does not have to be white
Should not have
• Any extraneous logo's or symbols

```html
<!DOCTYPE html>
<html lang="en">
<head>
<meta charset="utf-8">
<title>Morning Harbor Bible Fellowship – Business Card</title>
<link href="https://fonts.googleapis.com/css2?family=Montserrat:wght@300;400&family=Open+Sans:wght@400;700&display=swap" rel="stylesheet">
<style>
  :root {
    --backdrop: #222222;
    --brand-green: #4c8a47;
    --brand-olive: #7a7350;
    --ink: #333333;
    --rule: #9a9a9a;
    --paper: #ffffff;
  }
  * { margin: 0; padding: 0; box-sizing: border-box; }
  html, body { width: 1200px; height: 1200px; overflow: hidden; }
  body {
    background: var(--backdrop);
    display: flex;
    flex-direction: column;
    align-items: center;
    justify-content: center;
    gap: 64px;
    font-family: 'Open Sans', sans-serif;
  }
  .card {
    width: 900px;
    height: 514px;
    position: relative;
    box-shadow: 0 12px 30px rgba(0,0,0,0.5);
  }
  .card--front {
    background: var(--brand-green);
    display: flex;
    align-items: center;
    justify-content: center;
  }
  .wordmark {
    font-family: 'Montserrat', sans-serif;
    font-weight: 300;
    text-align: center;
    line-height: 1.15;
  }
  .wordmark__name { font-size: 58px; letter-spacing: 1px; }
  .wordmark__sub { font-size: 22px; letter-spacing: 9px; text-transform: uppercase; }
  .card--front .wordmark { color: var(--paper); }

  .card--back {
    background: var(--paper);
    display: flex;
    align-items: center;
  }
  .card--back .wordmark {
    color: var(--brand-green);
    width: 470px;
    padding-left: 50px;
  }
  .card--back .wordmark__name { font-size: 44px; }
  .card--back .wordmark__sub { font-size: 17px; letter-spacing: 6px; }
  .divider {
    width: 1px;
    height: 250px;
    background: var(--rule);
    margin-right: 40px;
  }
  .contact { color: var(--ink); font-size: 19px; line-height: 1.35; }
  .contact__name { color: var(--brand-green); font-weight: 700; font-size: 28px; line-height: 1.1; }
  .contact__role { color: var(--brand-olive); font-size: 19px; margin-bottom: 18px; }
  .contact__address { margin-bottom: 14px; }
  .contact__list { list-style: none; }
  .contact__list li { display: flex; align-items: center; gap: 10px; }
  .contact__list svg { width: 16px; height: 16px; fill: var(--brand-green); flex: none; }
</style>
</head>
<body>
  <section class="card card--front">
    <div class="wordmark">
      <div class="wordmark__name">Morning Harbor</div>
      <div class="wordmark__sub">Bible Fellowship</div>
    </div>
  </section>

  <section class="card card--back">
    <div class="wordmark">
      <div class="wordmark__name">Morning Harbor</div>
      <div class="wordmark__sub">Bible Fellowship</div>
    </div>
    <div class="divider"></div>
    <div class="contact">
      <div class="contact__name">Daniel Reyes</div>
      <div class="contact__role">General Manager</div>
      <div class="contact__address">48 Pier Lane, Harbor Point<br>P.O. Box 210, 12 Bay Avenue</div>
      <ul class="contact__list">
        <li><svg viewBox="0 0 16 16"><path d="M4 1l3 3-2 2c1 2 3 4 5 5l2-2 3 3-2 3C7 15 1 9 1 4z"/></svg>212-555-0147</li>
        <li><svg viewBox="0 0 16 16"><path d="M4 1h7v4H4zM1 6h14v6h-3v3H4v-3H1zM5 10v4h6v-4z"/></svg>212-555-0192</li>
        <li><svg viewBox="0 0 16 16"><path d="M1 3h14v10H1zM2 4l6 5 6-5z" fill-rule="evenodd"/></svg>hello@harborfellowship.org</li>
        <li><svg viewBox="0 0 16 16"><circle cx="8" cy="8" r="7" fill="none" stroke="#4c8a47" stroke-width="1.4"/><path d="M1 8h14M8 1c-3 4-3 10 0 14M8 1c3 4 3 10 0 14" fill="none" stroke="#4c8a47" stroke-width="1.2"/></svg>www.harborfellowship.org</li>
      </ul>
    </div>
  </section>
</body>
</html>
```